Company 10th Anniversary media design

We are celebrating the 10th Anniversary of Calder Ostrum Inc, a technology and professional services company, and we are looking for high-quality, creative, and premium anniversary media designs.

This project is to design anniversary branding and event visuals that reflect our 10-year journey, credibility, innovation, and growth. The designs will be used across event backdrops, photo booths, LinkedIn posts, and a short celebratory video, so consistency across all assets is very important.

Deliverables Required

10th Anniversary Logo / Emblem

A special “10 Years of Calder Ostrum” or “Calder Ostrum – 10th Anniversary” logo

Should complement (not replace) our existing company logo

Must work well in print, digital, and video formats

Main Event Backdrop Design

Large backdrop for stage or main celebration area

Should prominently feature:

Anniversary logo

Company name: Calder Ostrum Inc

Optional anniversary theme (e.g., “A Decade of Innovation & Growth”)

Clean, professional, and camera-friendly design

Photo Booth Backdrop

Engaging yet professional design for team and guest photos
Branding should be visible but not overpowering
Suitable for social media sharing
LinkedIn Post Design + Short Video
One or more LinkedIn-ready static post designs announcing the 10th anniversary
A short animated video (10–20 seconds) suitable for LinkedIn
Animation may include logo reveal, anniversary message, timeline highlights, or celebratory visuals
Design Style

Modern, corporate, and premium
Technology-driven look
Elegant celebration (not flashy or cartoonish)
Final deliverables should include print-ready and editable source files. High-quality submissions may lead to ongoing design work with our company.

Target Market(s)

IT Companies, Enterprise Clients, Technology Professionals, and IT Consultants

Industry/Entity Type

Information Technology

Font styles to use
Other font styles liked:
• MONTSERRAT

Colors
0094D4
00A9DD
6FCCEA
C7EBF8
E9F6FB
EB3D1F
EC4F4E
F09395
F8D3D4
FCEDEE

Requirements
Must have
• Clear 10th Anniversary message Professional, modern, technology-focused design Consistent branding across all deliverables Designs suitable for print, digital, and social media High-resolution and editable source files Corporate-friendly colors and typography
Nice to have
• Subtle tech elements (lines, grids, digital patterns, motion effects) Clean animation for the LinkedIn video Optional creative concept around “10-year journey” or “growth timeline” Minimal yet elegant celebratory accents
Should not have
• No cartoonish, childish, or overly playful visuals No cluttered layouts or excessive text No stock-heavy or generic anniversary templates Avoid overly flashy neon colors or gimmicky effects

```html
<!DOCTYPE html>
<html lang="en">
<head>
<meta charset="utf-8">
<title>Calder Ostrum – 10th Anniversary</title>
<link href="https://fonts.googleapis.com/css2?family=Montserrat:wght@300;400;500;600;700&display=swap" rel="stylesheet">
<style>
  :root {
    --stage: #6d6d6d;
    --blue: #1559a6;
    --blue-deep: #1670b6;
    --red: #e0261c;
    --red-deep: #c8231a;
    --white: #ffffff;
  }
  * { box-sizing: border-box; margin: 0; padding: 0; }
  html, body { width: 1009px; height: 1200px; overflow: hidden; }
  body {
    background: var(--stage);
    font-family: "Montserrat", sans-serif;
    position: relative;
  }

  /* Main stage backdrop */
  .backdrop {
    position: absolute;
    left: 16px; top: 22px;
    width: 977px; height: 651px;
    overflow: hidden;
    background: linear-gradient(125deg, #1676bd 0%, #1a62a6 28%, #4a4f78 50%, #a3302e 72%, var(--red-deep) 100%);
    color: var(--white);
  }
  .backdrop__globe {
    position: absolute;
    left: -40px; top: -60px;
    width: 300px; height: 300px;
    border-radius: 50%;
    background: radial-gradient(circle at 40% 55%, rgba(80,200,240,0.45) 0%, rgba(40,150,220,0.2) 45%, rgba(20,110,190,0) 70%);
  }
  .backdrop__name {
    position: absolute;
    left: 0; right: 0; top: 150px;
    text-align: center;
    font-size: 82px;
    font-weight: 700;
    letter-spacing: 2px;
    line-height: 1;
  }
  .emblem {
    position: absolute;
    left: 290px; top: 300px;
    display: flex;
    align-items: center;
    gap: 22px;
  }
  .emblem__number {
    font-size: 150px;
    font-weight: 300;
    line-height: 1;
    letter-spacing: -6px;
  }
  .emblem__words {
    font-size: 30px;
    font-weight: 500;
    line-height: 34px;
  }
  .backdrop__tagline {
    position: absolute;
    left: 0; right: 0; top: 440px;
    text-align: center;
    font-size: 27px;
    font-weight: 400;
  }

  /* Photo booth step-and-repeat */
  .booth {
    position: absolute;
    left: 16px; top: 690px;
    width: 977px; height: 488px;
    display: grid;
    grid-template-columns: repeat(6, 1fr);
    grid-template-rows: repeat(6, 1fr);
  }
  .tile {
    position: relative;
    display: flex;
    align-items: center;
    justify-content: center;
  }
  .tile--blue { background: var(--blue); color: var(--white); }
  .tile--white { background: var(--white); }
  .tile-emblem { flex-direction: column; }
  .tile-emblem__top { display: flex; align-items: center; gap: 6px; }
  .tile-emblem__number {
    font-size: 50px;
    font-weight: 700;
    line-height: 1;
    letter-spacing: -2px;
  }
  .tile-emblem__words { font-size: 10.5px; line-height: 11.5px; font-weight: 500; }
  .tile-emblem__tagline { font-size: 9px; margin-top: 6px; font-weight: 500; }
  .tile--white .tile-emblem__number { color: var(--red); }
  .tile--white .tile-emblem__words { color: var(--blue); }
  .tile--white .tile-emblem__tagline { color: #333; }
  .tile-name {
    font-size: 19px;
    font-weight: 700;
    letter-spacing: 0.5px;
  }
  .tile--white .tile-name { color: var(--red); }
  .tile--blue .tile-name { color: var(--white); }
</style>
</head>
<body>
  <section class="backdrop">
    <div class="backdrop__globe" role="img" aria-label="Glowing digital globe with connected network lines"></div>
    <h1 class="backdrop__name">Calder Ostrum</h1>
    <div class="emblem">
      <span class="emblem__number">10</span>
      <span class="emblem__words">Years<br>of Calder<br>Ostrum</span>
    </div>
    <p class="backdrop__tagline">A Decade of Innovation &amp; Growth</p>
  </section>

  <section class="booth">
    <!-- row 1 -->
    <div class="tile tile--blue tile-emblem"><div class="tile-emblem__top"><span class="tile-emblem__number">10</span><span class="tile-emblem__words">Years<br>of Calder<br>Ostrum</span></div><span class="tile-emblem__tagline">A Decade of Innovation &amp; Growth</span></div>
    <div class="tile tile--white"><span class="tile-name">Calder Ostrum</span></div>
    <div class="tile tile--blue tile-emblem"><div class="tile-emblem__top"><span class="tile-emblem__number">10</span><span class="tile-emblem__words">Years<br>of Calder<br>Ostrum</span></div><span class="tile-emblem__tagline">A Decade of Innovation &amp; Growth</span></div>
    <div class="tile tile--white"><span class="tile-name">Calder Ostrum</span></div>
    <div class="tile tile--blue tile-emblem"><div class="tile-emblem__top"><span class="tile-emblem__number">10</span><span class="tile-emblem__words">Years<br>of Calder<br>Ostrum</span></div><span class="tile-emblem__tagline">A Decade of Innovation &amp; Growth</span></div>
    <div class="tile tile--white"><span class="tile-name">Calder Ostrum</span></div>
    <!-- row 2 -->
    <div class="tile tile--white tile-emblem"><div class="tile-emblem__top"><span class="tile-emblem__number">10</span><span class="tile-emblem__words">Years<br>of Calder<br>Ostrum</span></div><span class="tile-emblem__tagline">A Decade of Innovation &amp; Growth</span></div>
    <div class="tile tile--blue"><span class="tile-name">Calder Ostrum</span></div>
    <div class="tile tile--white tile-emblem"><div class="tile-emblem__top"><span class="tile-emblem__number">10</span><span class="tile-emblem__words">Years<br>of Calder<br>Ostrum</span></div><span class="tile-emblem__tagline">A Decade of Innovation &amp; Growth</span></div>
    <div class="tile tile--blue"><span class="tile-name">Calder Ostrum</span></div>
    <div class="tile tile--white tile-emblem"><div class="tile-emblem__top"><span class="tile-emblem__number">10</span><span class="tile-emblem__words">Years<br>of Calder<br>Ostrum</span></div><span class="tile-emblem__tagline">A Decade of Innovation &amp; Growth</span></div>
    <div class="tile tile--blue"><span class="tile-name">Calder Ostrum</span></div>
    <!-- row 3 -->
    <div class="tile tile--blue tile-emblem"><div class="tile-emblem__top"><span class="tile-emblem__number">10</span><span class="tile-emblem__words">Years<br>of Calder<br>Ostrum</span></div><span class="tile-emblem__tagline">A Decade of Innovation &amp; Growth</span></div>
    <div class="tile tile--white"><span class="tile-name">Calder Ostrum</span></div>
    <div class="tile tile--blue tile-emblem"><div class="tile-emblem__top"><span class="tile-emblem__number">10</span><span class="tile-emblem__words">Years<br>of Calder<br>Ostrum</span></div><span class="tile-emblem__tagline">A Decade of Innovation &amp; Growth</span></div>
    <div class="tile tile--white"><span class="tile-name">Calder Ostrum</span></div>
    <div class="tile tile--blue tile-emblem"><div class="tile-emblem__top"><span class="tile-emblem__number">10</span><span class="tile-emblem__words">Years<br>of Calder<br>Ostrum</span></div><span class="tile-emblem__tagline">A Decade of Innovation &amp; Growth</span></div>
    <div class="tile tile--white"><span class="tile-name">Calder Ostrum</span></div>
    <!-- row 4 -->
    <div class="tile tile--white tile-emblem"><div class="tile-emblem__top"><span class="tile-emblem__number">10</span><span class="tile-emblem__words">Years<br>of Calder<br>Ostrum</span></div><span class="tile-emblem__tagline">A Decade of Innovation &amp; Growth</span></div>
    <div class="tile tile--blue"><span class="tile-name">Calder Ostrum</span></div>
    <div class="tile tile--white tile-emblem"><div class="tile-emblem__top"><span class="tile-emblem__number">10</span><span class="tile-emblem__words">Years<br>of Calder<br>Ostrum</span></div><span class="tile-emblem__tagline">A Decade of Innovation &amp; Growth</span></div>
    <div class="tile tile--blue"><span class="tile-name">Calder Ostrum</span></div>
    <div class="tile tile--white tile-emblem"><div class="tile-emblem__top"><span class="tile-emblem__number">10</span><span class="tile-emblem__words">Years<br>of Calder<br>Ostrum</span></div><span class="tile-emblem__tagline">A Decade of Innovation &amp; Growth</span></div>
    <div class="tile tile--blue"><span class="tile-name">Calder Ostrum</span></div>
    <!-- row 5 -->
    <div class="tile tile--blue tile-emblem"><div class="tile-emblem__top"><span class="tile-emblem__number">10</span><span class="tile-emblem__words">Years<br>of Calder<br>Ostrum</span></div><span class="tile-emblem__tagline">A Decade of Innovation &amp; Growth</span></div>
    <div class="tile tile--white"><span class="tile-name">Calder Ostrum</span></div>
    <div class="tile tile--blue tile-emblem"><div class="tile-emblem__top"><span class="tile-emblem__number">10</span><span class="tile-emblem__words">Years<br>of Calder<br>Ostrum</span></div><span class="tile-emblem__tagline">A Decade of Innovation &amp; Growth</span></div>
    <div class="tile tile--white"><span class="tile-name">Calder Ostrum</span></div>
    <div class="tile tile--blue tile-emblem"><div class="tile-emblem__top"><span class="tile-emblem__number">10</span><span class="tile-emblem__words">Years<br>of Calder<br>Ostrum</span></div><span class="tile-emblem__tagline">A Decade of Innovation &amp; Growth</span></div>
    <div class="tile tile--white"><span class="tile-name">Calder Ostrum</span></div>
    <!-- row 6 -->
    <div class="tile tile--white tile-emblem"><div class="tile-emblem__top"><span class="tile-emblem__number">10</span><span class="tile-emblem__words">Years<br>of Calder<br>Ostrum</span></div><span class="tile-emblem__tagline">A Decade of Innovation &amp; Growth</span></div>
    <div class="tile tile--blue"><span class="tile-name">Calder Ostrum</span></div>
    <div class="tile tile--white tile-emblem"><div class="tile-emblem__top"><span class="tile-emblem__number">10</span><span class="tile-emblem__words">Years<br>of Calder<br>Ostrum</span></div><span class="tile-emblem__tagline">A Decade of Innovation &amp; Growth</span></div>
    <div class="tile tile--blue"><span class="tile-name">Calder Ostrum</span></div>
    <div class="tile tile--white tile-emblem"><div class="tile-emblem__top"><span class="tile-emblem__number">10</span><span class="tile-emblem__words">Years<br>of Calder<br>Ostrum</span></div><span class="tile-emblem__tagline">A Decade of Innovation &amp; Growth</span></div>
    <div class="tile tile--blue"><span class="tile-name">Calder Ostrum</span></div>
  </section>
</body>
</html>
```